Business cards for Home & Garden Design business
Oakvale Grove Design
Business cards for Home & Garden Design business - Home and Garden
Creative Brief
Bright & Fun-filled
Marla Pendby
Designer
PO Box 732 Winkler, MB R6W 2K9
marlapendby@oakvalegrovedesign.example
oakvalegrovedesign.example
Would love to have my logo on a background of a rustic, white fence/door, or white birch trees. Question - do you already have access to my logo, or how do I upload it?

```html
<!DOCTYPE html>
<html lang="en">
<head>
<meta charset="utf-8">
<title>Oakvale Grove Design – Business Cards</title>
<link href="https://fonts.googleapis.com/css2?family=Raleway:wght@400;500;600&display=swap" rel="stylesheet">
<style>
  :root {
    --stage: #3b3b3e;
    --card-dark: #26262a;
    --card-light: #ffffff;
    --teal: #3a9aa0;
    --teal-light: #8fd3d7;
    --ink: #3a3a3e;
    --muted: #d9d9d9;
  }
  * { box-sizing: border-box; margin: 0; padding: 0; }
  html, body {
    width: 1200px; height: 670px; overflow: hidden;
    background: var(--stage);
    font-family: "Raleway", sans-serif;
  }
  .stage { position: relative; width: 1200px; height: 670px; }

  .card {
    position: absolute; width: 520px; height: 298px;
    border-radius: 4px; overflow: hidden;
    box-shadow: 0 10px 24px rgba(0,0,0,.35);
  }

  /* Back of card */
  .card-back { left: 50px; top: 90px; background: var(--card-dark); }
  .card-back .brand {
    position: absolute; inset: 0;
    display: flex; align-items: center; justify-content: center; gap: 14px;
  }
  .brand-name {
    font-weight: 500; font-size: 30px; letter-spacing: .5px;
    color: var(--teal-light);
  }
  .card-back .brand-dot {
    width: 22px; height: 22px; border-radius: 50%; background: var(--teal);
  }

  /* Front of card */
  .card-front { left: 630px; top: 282px; background: var(--card-light); }
  .card-front .wave { position: absolute; inset: 0; }
  .card-front .brand {
    position: absolute; left: 34px; top: 40px;
    display: flex; align-items: center; gap: 10px;
  }
  .card-front .brand-name { color: var(--teal); font-size: 22px; }
  .card-front .brand-dot {
    width: 16px; height: 16px; border-radius: 50%; background: var(--teal);
  }
  .person { position: absolute; left: 36px; top: 196px; }
  .person-name {
    font-size: 15px; font-weight: 500; letter-spacing: 1.5px;
    text-transform: uppercase; color: var(--teal);
  }
  .person-title { font-size: 11px; color: var(--ink); margin-top: 3px; }

  .contact {
    position: absolute; right: 22px; top: 108px;
    list-style: none; text-align: right;
    color: var(--muted); font-size: 8.5px; line-height: 1.4;
  }
  .contact li { display: flex; align-items: center; justify-content: flex-end; gap: 6px; }
  .contact .address { display: block; margin-bottom: 8px; }
  .contact li + li { margin-top: 3px; }
  .contact svg { width: 9px; height: 9px; flex: none; }
</style>
</head>
<body>
<main class="stage">

  <section class="card card-back" aria-label="Card back">
    <div class="brand">
      <span class="brand-name">Oakvale Grove Design</span>
      <span class="brand-dot" aria-hidden="true"></span>
    </div>
  </section>

  <section class="card card-front" aria-label="Card front">
    <svg class="wave" viewBox="0 0 520 298" preserveAspectRatio="none" aria-hidden="true">
      <path d="M0 262 C 130 260, 200 240, 255 175 C 315 110, 410 88, 520 82 L520 298 L0 298 Z" fill="var(--teal)"/>
      <path d="M0 276 C 140 274, 215 254, 272 188 C 330 124, 425 104, 520 100 L520 298 L0 298 Z" fill="var(--card-dark)"/>
    </svg>

    <div class="brand">
      <span class="brand-name">Oakvale Grove Design</span>
      <span class="brand-dot" aria-hidden="true"></span>
    </div>

    <div class="person">
      <p class="person-name">Marla Pendby</p>
      <p class="person-title">Designer</p>
    </div>

    <ul class="contact">
      <li class="address">PO Box 732<br>Winkler, MB R6W 2K9</li>
      <li>204 555 0148
        <svg viewBox="0 0 10 10"><path d="M2 1 L4 1 L5 3.5 L3.8 4.5 C4.4 5.8 5 6.4 6.3 7 L7.2 5.8 L9 6.8 L9 8.5 C5 9 1 5 1.5 1.5 Z" fill="var(--teal-light)"/></svg>
      </li>
      <li>204 555 0193
        <svg viewBox="0 0 10 10"><rect x="1.5" y="1.5" width="7" height="7" rx="1" fill="none" stroke="var(--teal-light)"/></svg>
      </li>
      <li>marlapendby@oakvalegrovedesign.example
        <svg viewBox="0 0 10 10"><rect x="1" y="2.5" width="8" height="5.5" fill="none" stroke="var(--teal-light)"/><path d="M1 2.5 L5 6 L9 2.5" fill="none" stroke="var(--teal-light)"/></svg>
      </li>
      <li>oakvalegrovedesign.example
        <svg viewBox="0 0 10 10"><circle cx="5" cy="5" r="4" fill="none" stroke="var(--teal-light)"/><path d="M1 5 H9 M5 1 V9" stroke="var(--teal-light)" stroke-width=".7"/></svg>
      </li>
    </ul>
  </section>

</main>
</body>
</html>
```